Morvex - Augmented Reality Mobile application

We need a logo design for new mobile application. The overall objective of the application is to build a digital content delivery tool for scanning and recognizing of an image (marker) through a mobile application. The provision of digital content to the user takes place via augmeted reality and / or redirecting the user to a given digital content source.We don`t have any color scheme yet, but we have been thinking about something colorful. We are open for ideas.I have uploaded our working logos, but we are not strongly engaged with them.
Updates

Hello everybody, I have increased the budget of the project Regards

Target Market(s)

Entertainment; Education;

Industry/Entity Type

Entertainment

Logo Text

"Morvex" is the name of the product. We want a logo enough distinguishable to be recognized even without the text

Font styles to use
Serif
Sans Serif

Colors

Designer to choose colors to be used in the design.

Requirements
Must have
• We have attached a document with some information about the product. Feel free to use whatever found useful in it.
• We are not looking for the same design, rather an alternative one. We need all of the screens mentioned in the document
Nice to have
Should not have

```html
<!DOCTYPE html>
<html lang="en">
<head>
<meta charset="utf-8">
<title>Morvex – Splash Screen</title>
<link rel="stylesheet" href="https://fonts.googleapis.com/css2?family=DM+Sans:wght@400;500;700&display=swap">
<style>
  :root {
    --page-bg: #ffffff;
    --screen-bg: #f5f5f6;
    --pattern-tint: #ece8fb;
    --pattern-lilac: #e2d6f7;
    --brand-purple: #5a0fe0;
    --heading-purple: #5200e0;
    --text-body: #1f1f24;
    --text-dark: #3b3b3d;
    --text-mid: #4a4a4c;
  }
  html, body {
    margin: 0;
    padding: 0;
    width: 1024px;
    height: 1200px;
    overflow: hidden;
    background: var(--page-bg);
    font-family: "DM Sans", sans-serif;
  }
  .board {
    position: relative;
    width: 1024px;
    height: 1200px;
    overflow: hidden;
  }

  /* soft background decorations */
  .deco {
    position: absolute;
    border-radius: 50%;
    background: var(--pattern-tint);
  }
  .deco--striped { width: 130px; height: 130px; opacity: 0.9; }
  .deco--dot-lg { width: 26px; height: 22px; }
  .deco--dot-sm { width: 12px; height: 10px; }

  /* intro copy */
  .intro {
    position: absolute;
    left: 134px;
    top: 150px;
    width: 360px;
  }
  .intro-title {
    margin: 0;
    font-size: 48px;
    font-weight: 700;
    line-height: 1.1;
    letter-spacing: -0.3px;
    color: var(--heading-purple);
  }
  .intro-text {
    margin: 36px 0 0;
    font-size: 15px;
    font-weight: 400;
    line-height: 1.5;
    letter-spacing: 0.2px;
    color: var(--text-body);
  }

  /* app screen */
  .splash-screen {
    position: absolute;
    left: 570px;
    top: 170px;
    width: 380px;
    height: 820px;
    background: var(--screen-bg);
    border-radius: 44px;
    overflow: hidden;
    box-shadow: 0 18px 40px rgba(40, 20, 90, 0.12), 0 0 0 1px #e6e6e8;
  }
  .confetti-pattern {
    position: absolute;
    inset: 0;
    background:
      radial-gradient(circle at 20% 15%, var(--pattern-lilac) 0, transparent 22%),
      radial-gradient(circle at 85% 55%, var(--pattern-lilac) 0, transparent 20%),
      radial-gradient(circle at 25% 82%, var(--pattern-lilac) 0, transparent 22%),
      var(--screen-bg);
  }
  .status-bar {
    position: absolute;
    top: 0;
    left: 0;
    right: 0;
    height: 50px;
    display: flex;
    align-items: center;
    justify-content: space-between;
    padding: 0 26px 0 30px;
    box-sizing: border-box;
    font-size: 13px;
    font-weight: 500;
    color: #111;
  }
  .status-icons { display: flex; gap: 6px; align-items: center; }
  .brand {
    position: absolute;
    top: 300px;
    left: 0;
    right: 0;
    display: flex;
    flex-direction: column;
    align-items: center;
  }
  .brand-mark {
    width: 140px;
    height: 140px;
    border-radius: 50%;
    background: var(--brand-purple);
    margin-bottom: 16px;
  }
  .brand-name {
    margin: 0;
    font-size: 28px;
    font-weight: 500;
    letter-spacing: 1px;
    color: var(--text-dark);
  }
  .brand-tagline {
    margin: 4px 0 0;
    font-size: 13px;
    font-weight: 400;
    color: var(--text-mid);
  }
</style>
</head>
<body>
  <main class="board">
    <div class="deco deco--striped" role="img" aria-label="Lilac diagonal-striped circle decoration" style="left:470px; top:-60px;"></div>
    <div class="deco deco--striped" role="img" aria-label="Lilac diagonal-striped circle decoration" style="left:280px; top:330px;"></div>
    <div class="deco deco--striped" role="img" aria-label="Lilac diagonal-striped circle decoration" style="left:480px; top:640px;"></div>
    <div class="deco deco--dot-lg" style="left:30px; top:360px;"></div>
    <div class="deco deco--dot-lg" style="left:566px; top:290px;"></div>
    <div class="deco deco--dot-lg" style="left:935px; top:70px;"></div>
    <div class="deco deco--dot-lg" style="left:280px; top:740px;"></div>
    <div class="deco deco--dot-sm" style="left:18px; top:62px;"></div>
    <div class="deco deco--dot-sm" style="left:205px; top:85px;"></div>
    <div class="deco deco--dot-sm" style="left:205px; top:420px;"></div>
    <div class="deco deco--dot-sm" style="left:430px; top:520px;"></div>
    <div class="deco deco--dot-sm" style="left:985px; top:500px;"></div>
    <div class="deco deco--dot-sm" style="left:110px; top:580px;"></div>
    <div class="deco deco--dot-sm" style="left:195px; top:860px;"></div>

    <section class="intro">
      <h1 class="intro-title">Splash Screen</h1>
      <p class="intro-text">Users are first greeted with this screen when they open the App.</p>
    </section>

    <section class="splash-screen">
      <div class="confetti-pattern" role="img" aria-label="Scattered lilac geometric confetti shapes: triangles, squiggles, crosses, cylinders and cubes"></div>

      <div class="status-bar">
        <span class="status-time">9:41</span>
        <span class="status-icons">
          <svg width="17" height="11" viewBox="0 0 22 14" aria-hidden="true">
            <rect x="0" y="10" width="3.5" height="4" rx="1" fill="#111"/>
            <rect x="6" y="7" width="3.5" height="7" rx="1" fill="#111"/>
            <rect x="12" y="4" width="3.5" height="10" rx="1" fill="#111"/>
            <rect x="18" y="0" width="3.5" height="14" rx="1" fill="#111"/>
          </svg>
          <svg width="15" height="11" viewBox="0 0 20 14" aria-hidden="true">
            <path d="M1 5 A13 13 0 0 1 19 5" fill="none" stroke="#111" stroke-width="2.2" stroke-linecap="round"/>
            <path d="M4.5 8.5 A8 8 0 0 1 15.5 8.5" fill="none" stroke="#111" stroke-width="2.2" stroke-linecap="round"/>
            <circle cx="10" cy="12" r="2" fill="#111"/>
          </svg>
          <svg width="23" height="11" viewBox="0 0 30 14" aria-hidden="true">
            <rect x="0.75" y="0.75" width="25" height="12.5" rx="3.5" fill="none" stroke="#111" stroke-width="1.5" opacity="0.5"/>
            <rect x="3" y="3" width="20.5" height="8" rx="2" fill="#111"/>
            <rect x="27" y="4.5" width="2" height="5" rx="1" fill="#111" opacity="0.5"/>
          </svg>
        </span>
      </div>

      <div class="brand">
        <div class="brand-mark"></div>
        <h2 class="brand-name">Morvex</h2>
        <p class="brand-tagline">Broaden your reality!</p>
      </div>
    </section>
  </main>
</body>
</html>
```